Corvallin Property Solutions need a business card design

Hello guys. We would need a business card design asap please.
We are a start up property investment business based in London UK specialised in buying, selling, managing and letting properties and helping distressed property owners.
The name of our Business is Corvallin, the logo symbolises the four fundamental elements of the world (earth, air, fire and water) and so it stands for strength, stability, longevity.
We would like the business card to communicate professionalism and reliability. Many many thanks indeed for your work.

Details:

1.) Marisol Dunkley
Property Investor
Mobile: +44(0)7700362517
Email: marisol.corvallin@quilbrook.example

2.) Tomas Brindle
Property Investor
Mobile: +44(0)7700845926
Email: tomas.corvallin@quilbrook.example

Industry/Entity Type

Investment

```html
<!DOCTYPE html>
<html lang="en">
<head>
<meta charset="utf-8">
<title>Corvallin Property Solutions – Business Card</title>
<link rel="stylesheet" href="https://fonts.googleapis.com/css2?family=Montserrat:wght@600;700&family=Lato:wght@400;700&display=swap">
<style>
  :root {
    --backdrop: #d9d9d9;
    --card: #141414;
    --brand-grey: #b9b9b9;
    --name-blue: #4f7fd6;
    --title-green: #2f9e3c;
    --label-red: #e0262f;
    --detail: #d8d8d8;
    --accent-red: #e3232f;
    --accent-blue: #3d6fc7;
    --accent-green: #1f9a35;
  }
  * { box-sizing: border-box; margin: 0; padding: 0; }
  html, body { width: 1200px; height: 926px; overflow: hidden; }
  body {
    background: var(--backdrop);
    position: relative;
    font-family: "Lato", Arial, sans-serif;
  }
  .card {
    position: absolute;
    left: 290px;
    width: 620px;
    height: 400px;
    background: var(--card);
    box-shadow: 0 6px 18px rgba(0,0,0,.25);
    overflow: hidden;
  }
  .card--back { top: 40px; }
  .card--front { top: 486px; }

  /* Back side */
  .brand-block {
    position: absolute;
    inset: 0;
    display: flex;
    flex-direction: column;
    align-items: center;
    justify-content: center;
    color: var(--brand-grey);
    font-family: "Montserrat", Arial, sans-serif;
    font-weight: 700;
  }
  .brand-mark {
    width: 70px; height: 70px;
    border-radius: 50%;
    background: var(--brand-grey);
    margin-bottom: 26px;
  }
  .brand-name { font-size: 40px; letter-spacing: 3px; line-height: 1; }
  .brand-tagline { font-size: 17px; letter-spacing: 1.5px; margin-top: 8px; }

  /* Front side */
  .accent-panel {
    position: absolute;
    left: 0; top: 0;
    width: 180px; height: 100%;
    background: linear-gradient(180deg, var(--accent-red) 0%, #f2f2f2 48%, var(--accent-blue) 70%, var(--accent-green) 100%);
    opacity: .92;
  }
  .contact-side {
    position: absolute;
    left: 250px; top: 52px;
    right: 30px;
  }
  .front-brand {
    font-family: "Montserrat", Arial, sans-serif;
    font-weight: 700;
    color: var(--brand-grey);
  }
  .front-brand .brand-name { font-size: 33px; letter-spacing: 2.5px; }
  .front-brand .brand-tagline { font-size: 14px; letter-spacing: 1.2px; margin-top: 4px; }
  .person { margin-top: 26px; }
  .person + .person { margin-top: 22px; }
  .person-name { color: var(--name-blue); font-size: 22px; line-height: 1.1; }
  .person-title { color: var(--title-green); font-size: 13px; letter-spacing: 1px; margin-bottom: 6px; }
  .person-line { color: var(--detail); font-size: 15px; line-height: 1.5; }
  .person-line .label { color: var(--label-red); font-weight: 700; }
</style>
</head>
<body>
  <section class="card card--back">
    <div class="brand-block">
      <span class="brand-mark"></span>
      <div class="brand-name">CORVALLIN</div>
      <div class="brand-tagline">PROPERTY SOLUTIONS</div>
    </div>
  </section>

  <section class="card card--front">
    <div class="accent-panel" role="img" aria-label="Large brand symbol decoration in red, white, blue and green"></div>
    <div class="contact-side">
      <div class="front-brand">
        <div class="brand-name">CORVALLIN</div>
        <div class="brand-tagline">PROPERTY SOLUTIONS</div>
      </div>
      <div class="person">
        <div class="person-name">Tomas Brindle</div>
        <div class="person-title">Property Investor</div>
        <div class="person-line"><span class="label">m:</span> +44(0)7700845926</div>
        <div class="person-line"><span class="label">e:</span> tomas.corvallin@quilbrook.example</div>
      </div>
      <div class="person">
        <div class="person-name">Marisol Dunkley</div>
        <div class="person-title">Property Investor</div>
        <div class="person-line"><span class="label">m:</span> +44(0)7700362517</div>
        <div class="person-line"><span class="label">e:</span> marisol.corvallin@quilbrook.example</div>
      </div>
    </div>
  </section>
</body>
</html>
```